Letterhead, stationery and email signature for construction business

I need the letterhead, stationery and email signature designs for a construction business. I want them to have a corporate feel to them.

I've attached the logo for reference.

```html
<!DOCTYPE html>
<html lang="en">
<head>
<meta charset="utf-8">
<title>Harlow Build Stationery</title>
<link rel="stylesheet" href="https://fonts.googleapis.com/css2?family=Montserrat:wght@400;500;600&display=swap">
<style>
  :root{
    --backdrop:#e4e4e4;
    --paper:#ffffff;
    --brand-blue:#2a56a6;
    --brand-slate:#545a66;
    --ink:#1c1c1c;
    --ink-soft:#3a3a3a;
    --faint:#f3f4f8;
  }
  *{margin:0;padding:0;box-sizing:border-box}
  html,body{width:1199px;height:1200px;overflow:hidden}
  body{position:relative;background:var(--backdrop);font-family:"Montserrat",Arial,sans-serif;color:var(--ink)}
  .sheet{position:absolute;background:var(--paper);overflow:hidden}
  .letterhead{left:102px;top:84px;width:622px;height:878px}
  .card-front{left:744px;top:206px;width:415px;height:242px}
  .card-back{left:744px;top:487px;width:415px;height:242px}
  .email-signature{left:412px;top:985px;width:625px;height:145px}

  .brand{position:absolute;display:flex;align-items:center;gap:8px;color:var(--brand-blue);font-weight:600;letter-spacing:.5px;white-space:nowrap}
  .brand-square{background:var(--brand-slate);flex:none}
  .brand-faint{position:absolute;background:var(--faint)}

  .letterhead .brand{left:42px;top:34px;font-size:24px}
  .letterhead .brand-square{width:32px;height:32px}
  .letterhead .brand-faint{left:223px;top:291px;width:399px;height:587px}

  .contact-list{position:absolute;list-style:none}
  .contact-list li{display:flex;align-items:center;gap:9px;color:var(--ink-soft);white-space:nowrap}
  .contact-list svg{width:9px;height:9px;fill:var(--ink);flex:none}
  .letterhead .contact-list{left:44px;top:784px;font-size:12.5px}
  .letterhead .contact-list li{height:17.5px}

  .card-front .brand{left:32px;top:30px;font-size:21px}
  .card-front .brand-square{width:28px;height:28px}
  .person-name{position:absolute;font-weight:600;white-space:nowrap}
  .person-role{position:absolute;white-space:nowrap}
  .card-front .person-name{left:34px;top:106px;font-size:16.5px}
  .card-front .person-role{left:34px;top:128px;font-size:9.5px;color:var(--ink-soft)}
  .card-front .contact-list{left:34px;top:156px;font-size:10px}
  .card-front .contact-list li{height:16px}
  .card-front .contact-list svg{width:7px;height:7px}

  .card-back .brand-faint{left:206px;top:12px;width:209px;height:218px}
  .card-back .brand{left:82px;top:98px;font-size:31px;gap:10px}
  .card-back .brand-square{width:40px;height:40px}

  .email-signature .band{position:absolute;left:0;top:0;width:625px;height:145px}
  .email-signature .band path{fill:var(--brand-blue)}
  .email-signature .brand{left:40px;top:52px;font-size:23px}
  .email-signature .brand-square{width:32px;height:32px}
  .email-signature .person-name{left:386px;top:24px;font-size:13.5px;color:var(--brand-blue)}
  .email-signature .person-role{left:386px;top:44px;font-size:9px;color:var(--ink-soft)}
  .email-signature .contact-list{left:386px;top:64px;font-size:9.5px}
  .email-signature .contact-list li{height:13.5px}
  .email-signature .contact-list svg{width:6.5px;height:6.5px;fill:var(--brand-blue)}
</style>
</head>
<body>

<svg width="0" height="0" style="position:absolute" aria-hidden="true">
  <symbol id="icon-phone" viewBox="0 0 10 10"><path d="M2.5 0h5a1 1 0 0 1 1 1v8a1 1 0 0 1-1 1h-5a1 1 0 0 1-1-1V1a1 1 0 0 1 1-1zm.5 1.5v6h4v-6z"/></symbol>
  <symbol id="icon-mail" viewBox="0 0 10 10"><path d="M0 2h10v6H0z"/></symbol>
  <symbol id="icon-web" viewBox="0 0 10 10"><path d="M5 0a5 5 0 1 1 0 10A5 5 0 0 1 5 0zm0 1.3a3.7 3.7 0 1 0 0 7.4 3.7 3.7 0 0 0 0-7.4z"/></symbol>
  <symbol id="icon-pin" viewBox="0 0 10 10"><path d="M5 0a3 3 0 0 1 3 3c0 2-3 4.5-3 4.5S2 5 2 3a3 3 0 0 1 3-3zM1 8.5h8V10H1z"/></symbol>
</svg>

<section class="sheet letterhead" aria-label="Letterhead">
  <div class="brand-faint" aria-hidden="true"></div>
  <div class="brand"><span class="brand-square"></span>HARLOW BUILD</div>
  <ul class="contact-list">
    <li><svg><use href="#icon-phone"/></svg>555-014-0192</li>
    <li><svg><use href="#icon-mail"/></svg>ks@harlowbuild.net</li>
    <li><svg><use href="#icon-web"/></svg>harlowbuild.net</li>
    <li><svg><use href="#icon-pin"/></svg>1200 Maple Ave. Westbrook, RJ 00000</li>
  </ul>
</section>

<section class="sheet card-front" aria-label="Business card front">
  <div class="brand"><span class="brand-square"></span>HARLOW BUILD</div>
  <div class="person-name">Kara Selwyn</div>
  <div class="person-role">Hair Stylist / Owner</div>
  <ul class="contact-list">
    <li><svg><use href="#icon-phone"/></svg>555-014-0192</li>
    <li><svg><use href="#icon-mail"/></svg>ks@harlowbuild.net</li>
    <li><svg><use href="#icon-web"/></svg>harlowbuild.net</li>
    <li><svg><use href="#icon-pin"/></svg>1200 Maple Ave. Westbrook, RJ 00000</li>
  </ul>
</section>

<section class="sheet card-back" aria-label="Business card back">
  <div class="brand-faint" aria-hidden="true"></div>
  <div class="brand"><span class="brand-square"></span>HARLOW BUILD</div>
</section>

<section class="sheet email-signature" aria-label="Email signature">
  <svg class="band" viewBox="0 0 625 145" aria-hidden="true">
    <path d="M264 0 L513 0 L588 61 L542 99 C548 45 520 8 264 0 Z"/>
  </svg>
  <div class="brand"><span class="brand-square"></span>HARLOW BUILD</div>
  <div class="person-name">Kara Selwyn</div>
  <div class="person-role">Hair Stylist / Owner</div>
  <ul class="contact-list">
    <li><svg><use href="#icon-phone"/></svg>555-014-0192</li>
    <li><svg><use href="#icon-mail"/></svg>ks@harlowbuild.net</li>
    <li><svg><use href="#icon-web"/></svg>harlowbuild.net</li>
    <li><svg><use href="#icon-pin"/></svg>1200 Maple Ave. Westbrook, RJ 00000</li>
  </ul>
</section>

</body>
</html>
```